Letterhead & Business Card Design Project

Use existing logo to create a new letterhead and business card design. Looking for something clean modern using color options of black, white and gray. The green from the logo may be used lightly as an accent color.

Target Market(s)

Professional business people

Industry/Entity Type

Business

Requirements
Must have
• Business card with front and back design using existing logo.
Nice to have
• Professional presentation
Clean look
Should not have
• No oil rigs, pumpjacks or clip art.

```html
<!DOCTYPE html>
<html lang="en">
<head>
<meta charset="utf-8">
<title>Halvard Exploration – Stationery</title>
<link href="https://fonts.googleapis.com/css2?family=Open+Sans:wght@400;600&display=swap" rel="stylesheet">
<style>
  :root{
    --bg:#9a9a9a;
    --paper:#f4f1f2;
    --card:#f1f1f1;
    --ink:#1a1a1a;
    --muted:#555;
    --green:#139a3a;
    --green-light:#2db14f;
  }
  *{box-sizing:border-box;margin:0;padding:0}
  html,body{width:1200px;height:720px;overflow:hidden}
  body{background:var(--bg);font-family:"Open Sans",sans-serif;color:var(--ink);position:relative}

  .brand{display:flex;align-items:center;gap:8px;font-weight:400;color:var(--ink);letter-spacing:.12em;text-transform:uppercase;white-space:nowrap}
  .brand-mark{width:8px;height:8px;background:var(--green);flex:none}

  /* Letterhead */
  .letterhead{position:absolute;left:40px;top:30px;width:467px;height:660px;background:var(--paper);box-shadow:0 4px 14px rgba(0,0,0,.25);overflow:hidden}
  .letterhead .brand{position:absolute;left:36px;top:72px;font-size:15px}
  .letterhead-contact{position:absolute;right:34px;top:34px;border-left:1.5px solid var(--green);padding-left:10px;font-size:9px;line-height:1.45;color:#333}
  .letter-body{position:absolute;left:50px;right:40px;top:140px;font-size:8.6px;line-height:1.55;color:#222}
  .letter-body p{margin-bottom:11px}
  .signature{position:absolute;left:110px;top:520px;font-size:10px}
  .letterhead-band{position:absolute;left:0;right:0;bottom:0;height:56px;background:var(--green);border-top:5px solid var(--paper);box-shadow:0 -3px 0 var(--ink);display:flex;align-items:center;justify-content:center;color:#fff;font-size:13px;letter-spacing:.55em}

  /* Business cards */
  .card{position:absolute;left:580px;width:560px;height:320px;background:var(--card);box-shadow:0 4px 14px rgba(0,0,0,.25);overflow:hidden}
  .card-front{top:30px}
  .card-back{top:370px;display:flex;align-items:center;justify-content:center}
  .card-front .brand{position:absolute;left:50px;top:150px;font-size:17px}
  .card-back .brand{font-size:30px;gap:14px}
  .card-back .brand-mark{width:14px;height:14px}
  .holder{position:absolute;left:330px;top:70px}
  .holder-name{font-size:17px;font-weight:600}
  .holder-role{font-size:14px;color:var(--green);margin-bottom:14px}
  .contact-list{list-style:none;font-size:13px;line-height:1.75}
  .contact-list li{display:flex;align-items:center;gap:9px}
  .contact-list svg{width:12px;height:12px;fill:var(--green);flex:none}
  .card-edge{position:absolute;left:0;bottom:0;width:100%;height:60px}
</style>
</head>
<body>

<section class="letterhead" aria-label="Letterhead">
  <div class="letterhead-contact">
    <div>555-010-2040</div>
    <div>info@halvard.com</div>
    <div>www.halvard.com</div>
  </div>
  <div class="brand"><span class="brand-mark"></span>Halvard Exploration</div>
  <div class="letter-body">
    <p>Lorem ipsum,</p>
    <p>Lorem ipsum dolor sit amet, consectetuer adipiscing elit. Nam cursus. Morbi ut mi. Nullam enim leo, egestas id, condimentum at, laoreet mattis, massa. Sed eleifend nonummy diam. Praesent mauris ante, elementum et, bibendum at, posuere sit amet, nibh. Duis tincidunt lectus quis dui viverra vestibulum. Suspendisse vulputate aliquam dui. Nulla elementum dui ut augue.</p>
    <p>Aliquam vehicula mi at mauris. Maecenas placerat, nisl at consequat rhoncus, sem nunc gravida justo, quis eleifend arcu velit quis lacus. Morbi magna magna, tincidunt a, mattis non, imperdiet vitae, tellus.</p>
    <p>Pellentesque habitant morbi tristique senectus et netus et malesuada fames ac turpis egestas. Maecenas posuere felis nec tortor. Pellentesque faucibus. Ut accumsan ultricies elit. Maecenas at justo id velit placerat molestie. Donec dictum lectus non odio. Cras a ante vitae enim iaculis aliquam.</p>
    <p>Mauris nunc quam, venenatis nec, euismod sit amet, egestas placerat, est. Pellentesque habitant morbi tristique senectus et netus et malesuada fames ac turpis egestas. Cras id elit. Integer quis urna.</p>
  </div>
  <div class="signature">Director</div>
  <footer class="letterhead-band">www.halvard.com</footer>
</section>

<section class="card card-front" aria-label="Business card front">
  <div class="brand"><span class="brand-mark"></span>Halvard Exploration</div>
  <div class="holder">
    <div class="holder-name">John Doe</div>
    <div class="holder-role">Director</div>
    <ul class="contact-list">
      <li><svg viewBox="0 0 24 24"><path d="M6.6 10.8a15 15 0 0 0 6.6 6.6l2.2-2.2c.3-.3.7-.4 1-.2 1.1.4 2.3.6 3.6.6.6 0 1 .4 1 1V20c0 .6-.4 1-1 1A17 17 0 0 1 3 4c0-.6.4-1 1-1h3.5c.6 0 1 .4 1 1 0 1.3.2 2.5.6 3.6.1.3 0 .7-.2 1z"/></svg>555-010-2040</li>
      <li><svg viewBox="0 0 24 24"><path d="M2 5h20v14H2zm2 2v.5l8 5 8-5V7l-8 5z"/></svg>info@halvard.com</li>
      <li><svg viewBox="0 0 24 24"><path d="M12 2a7 7 0 0 0-7 7c0 5 7 13 7 13s7-8 7-13a7 7 0 0 0-7-7zm0 9.5A2.5 2.5 0 1 1 12 6.5a2.5 2.5 0 0 1 0 5z"/></svg>www.halvard.com</li>
    </ul>
  </div>
  <svg class="card-edge" viewBox="0 0 560 60" preserveAspectRatio="none" aria-hidden="true">
    <polygon points="0,52 420,52 440,40 560,40 560,60 0,60" fill="var(--ink)"/>
    <polygon points="440,40 460,28 560,28 560,40" fill="var(--green)"/>
  </svg>
</section>

<section class="card card-back" aria-label="Business card back">
  <div class="brand"><span class="brand-mark"></span>Halvard Exploration</div>
</section>

</body>
</html>
```